Business Advisory Firm Business Card

A clean, very upscale looking business card. Not crowded.

Please include logo (attached) and:

Daria K. Pellworth
Four Marlow Court
New York, NY 10023
tel: (917) 555-0143
fax: (646) 555-0172
email: dpellworth@quarrystoneconsultants.example
website: www.quarrystoneconsultants.example

Target Market(s)

Business clients. Often real estate development firms, other advisory firms or growing companies that need assistance. I would like a card that looks impressive and confident.

Industry/Entity Type

Business

Colors

Designer to choose colors to be used in the design.

Requirements
Must have
• Impressive and confident. Please include logo.
Should not have
• nothing flashy...

```html
<!DOCTYPE html>
<html lang="en">
<head>
<meta charset="utf-8">
<title>Quarrystone Advisory Services – Business Card</title>
<link rel="stylesheet" href="https://fonts.googleapis.com/css2?family=Mulish:wght@400;600;700&display=swap">
<style>
  :root {
    --backdrop: #e9e7e4;
    --card-white: #ffffff;
    --card-dark: #1a1e1e;
    --pattern-dark: #2a2f2f;
    --band-grey: #a9aaab;
    --band-grey-dark: #8d8e90;
    --brand-green: #a8d44c;
    --text-grey: #5b5c5e;
    --text-dark: #1f2021;
    --text-body: #2c2d2e;
  }
  * { box-sizing: border-box; margin: 0; padding: 0; }
  html, body { width: 1200px; height: 800px; overflow: hidden; }
  body {
    background: var(--backdrop);
    font-family: "Mulish", sans-serif;
    position: relative;
  }
  .card {
    position: absolute;
    top: 245px;
    width: 540px;
    height: 309px;
    overflow: hidden;
    box-shadow: 0 6px 18px rgba(0,0,0,0.18);
  }

  /* ---------- Back of card ---------- */
  .card-back { left: 40px; background: var(--card-dark); }
  .card-back .pattern-field {
    position: absolute; inset: 0;
    background: linear-gradient(135deg, var(--pattern-dark) 0%, var(--card-dark) 55%, #141717 100%);
  }
  .card-back .brand {
    position: absolute; left: 34px; top: 34px;
    display: flex; align-items: flex-start; gap: 16px;
  }
  .brand-square { width: 46px; height: 46px; flex: none; }
  .card-back .brand-square { background: var(--brand-green); }
  .brand-name {
    font-weight: 600;
    font-variant: small-caps;
    letter-spacing: 1px;
    line-height: 1;
  }
  .card-back .brand-name { color: var(--brand-green); font-size: 22px; }
  .card-back .website {
    position: absolute; right: 30px; bottom: 26px;
    color: var(--brand-green);
    font-size: 15px; letter-spacing: 0.3px;
  }

  /* ---------- Front of card ---------- */
  .card-front { left: 620px; background: var(--card-white); }
  .card-front .corner-band { position: absolute; left: 0; top: 0; }
  .card-front .brand {
    position: absolute; left: 84px; top: 18px;
    display: flex; align-items: flex-start; gap: 18px;
  }
  .card-front .brand-square { background: var(--brand-green); width: 54px; height: 54px; }
  .card-front .brand-name {
    color: var(--text-grey); font-size: 23px; margin-top: 26px;
  }
  .holder-name {
    position: absolute; left: 100px; top: 130px;
    color: var(--text-dark);
    font-weight: 700; font-size: 17px; letter-spacing: 0.6px;
    text-transform: uppercase;
  }
  .contact-list {
    position: absolute; left: 100px; top: 164px;
    list-style: none;
    color: var(--text-body); font-size: 13px; line-height: 20px;
  }
  .contact-list li { display: flex; align-items: center; gap: 8px; }
  .contact-icon {
    width: 12px; height: 12px; flex: none;
    background: var(--brand-green); border-radius: 2px;
    display: flex; align-items: center; justify-content: center;
  }
  .address {
    position: absolute; left: 100px; top: 232px;
    color: var(--text-body); font-size: 13px; letter-spacing: 0.4px;
    text-transform: uppercase;
  }
</style>
</head>
<body>

<section class="card card-back" aria-label="Card back">
  <div class="pattern-field" role="img" aria-label="Dark geometric cube pattern background"></div>
  <div class="brand">
    <span class="brand-square"></span>
    <p class="brand-name">Quarrystone<br>Advisory<br>Services, Inc.</p>
  </div>
  <p class="website">www.quarrystoneconsultants.example</p>
</section>

<section class="card card-front" aria-label="Card front">
  <svg class="corner-band" width="540" height="309" viewBox="0 0 540 309" aria-hidden="true">
    <polygon points="0,0 170,0 70,100 0,170" fill="var(--band-grey)"/>
    <polygon points="0,170 70,100 80,110 0,190" fill="var(--band-grey-dark)"/>
  </svg>
  <div class="brand">
    <span class="brand-square"></span>
    <p class="brand-name">Quarrystone<br>Advisory<br>Services, Inc.</p>
  </div>
  <p class="holder-name">Daria K. Pellworth</p>
  <ul class="contact-list">
    <li>
      <span class="contact-icon">
        <svg width="8" height="8" viewBox="0 0 8 8" aria-hidden="true"><path d="M1.5 1 L3 1 L3.5 2.6 L2.6 3.2 Q3.3 4.7 4.8 5.4 L5.4 4.5 L7 5 L7 6.5 Q3.5 7 1 2.5 Z" fill="#fff"/></svg>
      </span>(917) 555-0143
    </li>
    <li>
      <span class="contact-icon">
        <svg width="8" height="8" viewBox="0 0 8 8" aria-hidden="true"><rect x="1" y="3" width="6" height="4" fill="#fff"/><rect x="2" y="1" width="4" height="2" fill="#fff"/></svg>
      </span>(646) 555-0172
    </li>
    <li>
      <span class="contact-icon">
        <svg width="8" height="8" viewBox="0 0 8 8" aria-hidden="true"><rect x="0.5" y="1.5" width="7" height="5" fill="none" stroke="#fff"/><path d="M0.5 1.5 L4 4.5 L7.5 1.5" fill="none" stroke="#fff"/></svg>
      </span>dpellworth@quarrystoneconsultants.example
    </li>
  </ul>
  <p class="address">Four Marlow Court, New York, NY 10023</p>
</section>

</body>
</html>
```